Brochure Design Project

We are a payroll company. We offer a wide variety of products and services:
1. Payroll Processing
2. Employee Direct Deposit
3. Time and attendance
4. HR services
5. Employee Employee Benefits

I'd like to develop a one page template that uses a combination of our logo (attached), colors (attached) and possible a picture. The picture could be shown as an option as it may change based on the product or service.

Target Market(s)

Adults in the United States ages 22-50. Typically these people are accountants, human resource professionals or entrepreneurs. The payroll industry is dominated by 3 large payroll processors, KLV, Wendorn and Tolvaris. These companies are very impersonal and make it difficult to resolve issues when they arise. We have grown to over 400 clients by being the opposite of the big guys,

Industry/Entity Type

It Company

Font styles to use
Sans Serif

Requirements
Must have
• The brochure can be one or two pages.
Nice to have
• I'll know it when I see it but I can't describe it. I have attached a few brochures that have caught my eye.
Should not have
• No cartoons. No money signs. Hip, new, fresh are words I'd use to describe the winning product. Of the three people I described in my target market, the entrepreneur is the market I'd most like to target.

```html
<!DOCTYPE html>
<html lang="en">
<head>
<meta charset="utf-8">
<title>Ledgerline Payroll – Services Brochure</title>
<link rel="stylesheet" href="https://fonts.googleapis.com/css2?family=Open+Sans:wght@400;700&display=swap">
<style>
  :root {
    --navy: #213469;
    --green: #7bc043;
    --white: #ffffff;
    --paper: #ffffff;
    --backdrop: #e4e4e4;
    --muted: #5b6a8f;
  }
  * { box-sizing: border-box; margin: 0; padding: 0; }
  html, body { width: 1200px; height: 1000px; overflow: hidden; }
  body {
    background: var(--backdrop);
    font-family: "Open Sans", Arial, sans-serif;
    position: relative;
  }
  .brochure {
    position: absolute;
    left: 100px; top: 150px;
    width: 1000px; height: 700px;
    background: var(--paper);
    overflow: hidden;
  }
  .services-panel {
    position: absolute; left: 0; top: 0;
    width: 1000px; height: 560px;
    background: var(--navy);
  }
  .connector-map {
    position: absolute; left: 0; top: 0;
    width: 1000px; height: 560px;
  }
  .service {
    position: absolute;
    color: var(--white);
    display: flex; flex-direction: column; align-items: center;
  }
  .service-icon { width: 80px; height: 60px; display: block; }
  .service-title {
    font-weight: 700; font-size: 14px; line-height: 20px;
    text-align: center; margin: 8px 0 6px;
  }
  .service-text {
    font-size: 11px; line-height: 1.45;
    text-align: justify; hyphens: auto;
  }
  .service--support    { left: 30px;  top: 100px; width: 190px; }
  .service--managed    { left: 250px; top: 175px; width: 200px; }
  .service--consulting { left: 490px; top: 265px; width: 210px; }
  .service--hosted     { left: 740px; top: 300px; width: 230px; }

  .tagline-tab {
    position: absolute; left: 0; top: 480px;
    width: 240px; height: 80px;
    background: var(--green);
    border-radius: 0 0 60px 0;
    color: var(--white);
    font-weight: 700; font-size: 26px;
    display: flex; align-items: center; padding-left: 20px;
  }
  .website {
    position: absolute; left: 200px; top: 618px;
    font-size: 13px; letter-spacing: 3px;
    color: var(--muted);
  }
  .brand-name {
    position: absolute; right: 50px; top: 596px;
    font-weight: 700; font-size: 44px; line-height: 60px;
    color: var(--navy);
    display: flex; align-items: center; gap: 14px;
  }
  .brand-dot {
    width: 26px; height: 26px; border-radius: 50%;
    background: var(--green);
  }
</style>
</head>
<body>
  <main class="brochure">
    <section class="services-panel">
      <svg class="connector-map" viewBox="0 0 1000 560" aria-hidden="true">
        <g fill="none" stroke="#ffffff" stroke-width="2" stroke-dasharray="2 4">
          <path d="M125 60 H530"/>
          <path d="M125 60 V98"/>
          <path d="M350 173 V150 H855 V298"/>
          <path d="M595 130 V263"/>
        </g>
        <g fill="#ffffff">
          <circle cx="125" cy="60" r="4"/>
          <circle cx="855" cy="150" r="4"/>
          <circle cx="350" cy="150" r="4"/>
        </g>
        <circle cx="595" cy="65" r="62" fill="none" stroke="#ffffff" stroke-width="3" stroke-dasharray="2 5"/>
        <circle cx="595" cy="65" r="48" fill="#ffffff"/>
      </svg>

      <article class="service service--support">
        <svg class="service-icon" viewBox="0 0 80 60" aria-hidden="true">
          <rect x="5" y="4" width="70" height="52" rx="8" fill="#ffffff"/>
          <rect x="49" y="22" width="28" height="16" rx="4" fill="#213469"/>
          <circle cx="59" cy="30" r="3" fill="#ffffff"/>
        </svg>
        <h3 class="service-title">Service</h3>
        <p class="service-text">Our Support Services package has been specifically designed to provide our clients with a flexible I.T solution that has no lock in contract terms. This service package allows for the purchase of block hours that can be utilised at any time and which never expire.</p>
      </article>
      <article class="service service--managed">
        <svg class="service-icon" viewBox="0 0 80 60" aria-hidden="true">
          <rect x="3" y="5" width="74" height="50" rx="8" fill="none" stroke="#ffffff" stroke-width="5"/>
          <rect x="3" y="17" width="74" height="7" fill="#ffffff"/>
          <rect x="50" y="35" width="15" height="9" fill="#ffffff"/>
        </svg>
        <h3 class="service-title">Service</h3>
        <p class="service-text">Our Managed Services package is Norvane's outsourcing service and is an excellent way to assist our clients with delivering against all their internal business I.T needs. What makes this particular service unique is it greatly reduces (and often removes) the need for expensive internal I.T resources normally dedicated to maintaining and improving a business's I.T systems.</p>
      </article>
      <article class="service service--consulting">
        <svg class="service-icon" viewBox="0 0 80 60" aria-hidden="true">
          <rect x="29" y="4" width="22" height="12" rx="3" fill="none" stroke="#ffffff" stroke-width="4"/>
          <rect x="5" y="14" width="70" height="42" rx="6" fill="#ffffff"/>
          <rect x="5" y="29" width="70" height="3" fill="#213469"/>
          <rect x="35" y="25" width="10" height="10" fill="#213469"/>
        </svg>
        <h3 class="service-title">Service</h3>
        <p class="service-text">Our Consulting Services is an excellent way for our clients to access the expert skills and years of knowledge held with our I.T Engineers. This expertise is most commonly used for small, medium and large project works, to bridge implementation knowledge gaps and/or to assist with the strategic planning of I.T solutions.</p>
      </article>
      <article class="service service--hosted">
        <svg class="service-icon" viewBox="0 0 80 60" aria-hidden="true">
          <rect x="15" y="0" width="50" height="60" rx="4" fill="#ffffff"/>
          <g fill="#213469">
            <rect x="22" y="7" width="6" height="6"/><rect x="32" y="7" width="6" height="6"/><rect x="42" y="7" width="6" height="6"/><rect x="52" y="7" width="6" height="6"/>
            <rect x="22" y="19" width="6" height="6"/><rect x="32" y="19" width="6" height="6"/><rect x="42" y="19" width="6" height="6"/><rect x="52" y="19" width="6" height="6"/>
            <rect x="22" y="31" width="6" height="6"/><rect x="32" y="31" width="6" height="6"/><rect x="42" y="31" width="6" height="6"/><rect x="52" y="31" width="6" height="6"/>
            <rect x="22" y="43" width="6" height="6"/><rect x="32" y="43" width="6" height="6"/><rect x="42" y="43" width="6" height="6"/><rect x="52" y="43" width="6" height="6"/>
          </g>
        </svg>
        <h3 class="service-title">Service</h3>
        <p class="service-text">Is your current I.T solution too expensive, outdated, hard to understand or a huge drain on your internal resources? Do you want to remove the headache of dealing with the day to day management that goes with maintaining a highly efficient I.T system? Then Norvane's fully hosted services may be the perfect fit for your business.</p>
      </article>
    </section>

    <div class="tagline-tab">a Payroll Partner.</div>
    <p class="website">www.ledgerlinepayroll.com</p>
    <div class="brand-name"><span class="brand-dot"></span>Ledgerline Payroll</div>
  </main>
</body>
</html>
```